PrairieKite - New Website Design

Create a professional Shopify website for the hottest trend; a box of school supplies subscription box business called PrairieKite. Wexelo.com is an easy to use website builder.
Please see fernwhistle.com; lunapebble.com; quietmeadowfolk.com; and tovinjar.com for the concept I am after. The business has not been launched yet, I am currently in the pre-launch stage using a specialized landing page website, and so the time scale for developing my professional looking Shopify website is up to 1-2 weeks.
The webpage should have a fun feel and should match the style of the company logo at lunapebble.com. The pages to include are 'Home', 'About us' and 'Get Started'
Thank you and good luck!

```html
<!DOCTYPE html>
<html lang="en">
<head>
<meta charset="utf-8">
<title>PrairieKite – About Us</title>
<link rel="stylesheet" href="https://fonts.googleapis.com/css2?family=Roboto:wght@300;400;500;700&family=Roboto+Condensed:wght@400;700&family=Montserrat:wght@400;500;800&display=swap">
<style>
:root{
  --orange:#f65c1f;
  --ink:#2b2b2b;
  --dark:#2e2e2e;
  --grey:#6a6a6a;
  --muted:#8c8c8c;
  --footer-bg:#ececec;
  --white:#ffffff;
}
*{margin:0;padding:0;box-sizing:border-box}
html,body{width:1200px;height:1134px;overflow:hidden;background:var(--white)}
body{position:relative;font-family:"Roboto",sans-serif;color:var(--ink)}
.abs{position:absolute}

/* header */
.site-header{left:0;top:0;width:1200px;height:54px;background:var(--white);border-bottom:1px solid #e2e2e2;z-index:2}
.brand{left:160px;top:13px;font-family:"Montserrat",sans-serif;font-weight:800;font-size:22px;line-height:28px;color:var(--orange);letter-spacing:.5px}
.nav{top:19px;font-weight:500;font-size:13px;line-height:16px;color:var(--ink);letter-spacing:.2px}
.nav.active{color:var(--orange)}
.icon{top:18px}
.cart-count{left:1004px;top:21px;font-size:10px;font-weight:700}

/* hero */
.hero{left:0;top:54px;width:1200px;height:488px;background:linear-gradient(180deg,#e9e9e9 0%,#f6f6f6 100%)}
.hero-photo{left:665px;top:30px;width:535px;height:458px;background:linear-gradient(135deg,#f5d54a 0%,#f27a35 25%,#e33c5a 45%,#7a4fc1 62%,#2d7ad6 78%,#2aa866 100%);clip-path:polygon(25% 0,100% 0,100% 100%,0 100%,0 88%,18% 60%,21% 8%)}
.hero-title{left:160px;top:48px;font-weight:500;font-size:43px;line-height:50px;color:var(--ink)}
.hero-sub{left:160px;top:100px;width:380px;font-size:17.5px;line-height:21px;color:var(--ink)}
.hero-copy{left:160px;top:163px;font-weight:400;font-size:14.6px;line-height:22.4px;color:var(--grey);white-space:nowrap}
.feature{left:160px;font-weight:500;font-size:15px;line-height:20px;color:var(--orange)}

/* promo */
.promo{left:0;top:542px;width:822px;height:256px;background:var(--orange)}
.promo-photo{left:345px;top:0;width:477px;height:256px;background:linear-gradient(90deg,rgba(246,92,31,0) 0%,#f2c98a 22%,#f3d23a 45%,#1f5fc2 80%,#1a4fa8 100%);clip-path:polygon(0 100%,28% 40%,40% 0,100% 0,100% 100%)}
.sale-title{left:92px;top:20px;font-family:"Montserrat",sans-serif;font-weight:800;font-size:46px;line-height:56px;color:var(--white)}
.sale-sub{left:92px;top:82px;font-family:"Montserrat",sans-serif;font-weight:400;font-size:30px;line-height:36px;color:var(--white)}
.sale-sub em{font-style:normal;color:var(--ink)}
.sale-arrow{left:452px;top:90px}
.shipping{left:822px;top:542px;width:378px;height:256px;background:var(--dark)}
.ship-title{left:25px;top:20px;font-family:"Montserrat",sans-serif;font-weight:500;font-size:32px;line-height:40px;color:var(--white)}
.ship-sub{left:25px;top:67px;font-family:"Montserrat",sans-serif;font-weight:500;font-size:24px;line-height:30px;color:var(--white)}
.ship-sub span{color:var(--orange)}
.ship-note{left:25px;top:104px;width:280px;font-family:"Montserrat",sans-serif;font-size:16px;line-height:18px;color:var(--muted)}

/* newsletter */
.connect{left:0;top:798px;width:1200px;height:98px;background:var(--orange)}
.band-heading{top:32px;font-family:"Roboto Condensed",sans-serif;font-weight:700;font-size:27px;line-height:34px;color:var(--white)}
.email{left:361px;top:29px;width:359px;height:42px;background:var(--white);border-radius:5px;overflow:hidden}
.email-field{left:15px;top:13px;font-weight:300;font-size:13px;color:#999}
.go{left:309px;top:0;width:50px;height:42px;background:var(--ink);color:var(--white);font-family:"Roboto Condensed",sans-serif;font-weight:700;font-size:22px;display:flex;align-items:center;justify-content:center}
.social{top:34px;height:32px;padding:0 8px;border-radius:5px;background:var(--white);color:var(--orange);font-family:"Roboto Condensed",sans-serif;font-weight:700;font-size:14px;display:flex;align-items:center}

/* footer */
.footer{left:0;top:896px;width:1200px;height:238px;background:var(--footer-bg)}
.col{top:36px}
.col h3{font-family:"Roboto Condensed",sans-serif;font-weight:400;font-size:18.5px;line-height:22px;color:#555;margin-bottom:5px}
.col a{display:block;font-weight:300;font-size:12.5px;line-height:22.4px;color:#555;text-decoration:none}
.rule{left:160px;top:186px;width:880px;height:1px;background:#d6d6d6}
.copyright{left:160px;top:200px;font-weight:300;font-size:12px;color:#666}
.pay{top:196px;width:26px;height:17px;border-radius:2px}
</style>
</head>
<body>

<header class="site-header abs">
  <div class="brand abs">PrairieKite</div>
  <span class="nav abs" style="left:676px">HOME</span>
  <span class="nav active abs" style="left:736px">ABOUT US</span>
  <span class="nav abs" style="left:825px">GET STARTED</span>
  <svg class="icon abs" style="left:949px" width="16" height="16" viewBox="0 0 16 16" aria-label="Search"><circle cx="6.5" cy="6.5" r="5" fill="none" stroke="#2b2b2b" stroke-width="1.6"/><line x1="10" y1="10" x2="15" y2="15" stroke="#2b2b2b" stroke-width="1.8"/></svg>
  <svg class="icon abs" style="left:985px;top:17px" width="15" height="17" viewBox="0 0 15 17" aria-label="Cart"><path d="M4 5V3.5a3.5 3.5 0 0 1 7 0V5" fill="none" stroke="#2b2b2b" stroke-width="1.5"/><rect x="0.5" y="5" width="14" height="11.5" fill="#2b2b2b"/></svg>
  <span class="cart-count abs">0</span>
  <svg class="icon abs" style="left:1025px" width="15" height="16" viewBox="0 0 15 16" aria-label="Account"><circle cx="7.5" cy="4.5" r="4" fill="#2b2b2b"/><path d="M0 16c0-5 3-7 7.5-7S15 11 15 16z" fill="#2b2b2b"/></svg>
</header>

<section class="hero abs">
  <div class="hero-photo abs" role="img" aria-label="Photo of open tins of rainbow-coloured pencils"></div>
  <h1 class="hero-title abs">ABOUT US</h1>
  <p class="hero-sub abs">Catering to your requirements, handling<br>your needs with care.</p>
  <p class="hero-copy abs">Our store is more than just another average online retailer. We sell<br>not only top quality products, but give our customers a positive<br>online shopping experience. Forget about struggling to do everything<br>at once: taking care of the family, running your business, walking<br>your dog, cleaning the house, doing the shopping, etc. Purchase the<br>goods you need every day or just like in a few clicks or taps,<br>depending on the device you use to access the Internet. We work to<br>make your life more enjoyable.</p>
  <span class="feature abs" style="top:366px">Top quality products</span>
  <span class="feature abs" style="top:392px">Best customer service</span>
  <span class="feature abs" style="top:419px">30-days money back guarantee</span>
</section>

<section class="promo abs">
  <div class="promo-photo abs" role="img" aria-label="Photo of two smiling schoolgirls holding coloured pencils"></div>
  <div class="sale-title abs">BIG SALE:</div>
  <div class="sale-sub abs">SAVE UP TO <em>30%</em> OFF</div>
  <svg class="sale-arrow abs" width="14" height="22" viewBox="0 0 14 22" aria-hidden="true"><path d="M3 2l9 9-9 9" fill="none" stroke="#fff" stroke-width="2.5"/></svg>
</section>

<section class="shipping abs">
  <div class="ship-title abs">Free shipping</div>
  <div class="ship-sub abs">ON ORDERS OVER <span>$99</span></div>
  <p class="ship-note abs">This offer is valid on all our store items</p>
</section>

<section class="connect abs">
  <div class="band-heading abs" style="left:160px">Stay Connected</div>
  <div class="email abs">
    <span class="email-field abs">Enter your email address...</span>
    <div class="go abs">GO</div>
  </div>
  <div class="band-heading abs" style="left:755px">Get social</div>
  <span class="social abs" style="left:880px">Chatterly</span>
  <span class="social abs" style="left:960px">Flitter</span>
</section>

<footer class="footer abs">
  <div class="col abs" style="left:160px"><h3>Stay Connected</h3><a href="#">Sign in</a><a href="#">Create account</a></div>
  <div class="col abs" style="left:367px"><h3>Products</h3><a href="#">About us</a><a href="#">Brand</a><a href="#">Contact us</a><a href="#">Gift certificates</a><a href="#">Sitemap</a></div>
  <div class="col abs" style="left:560px"><h3>Customer Service</h3><a href="#">About your order</a><a href="#">Wishlist</a></div>
  <div class="col abs" style="left:767px"><h3>Safety &amp; Security</h3><a href="#">Our team</a><a href="#">Privacy policy</a></div>
  <div class="rule abs"></div>
  <div class="copyright abs">© 2017 PrairieKite. Powered by</div>
  <span class="pay abs" style="left:915px;background:#3d4a8a"></span>
  <span class="pay abs" style="left:947px;background:#ffffff;border:1px solid #ccc"></span>
  <span class="pay abs" style="left:980px;background:#d8322a"></span>
  <span class="pay abs" style="left:1013px;background:#ffffff;border:1px solid #ccc"></span>
</footer>

</body>
</html>
```